Tavrelo LLC banner ad design project

I want banner advertisements designed in various ad formats-the most popular sizes according to Plinkora Spots (600x450, 300x250, 250x250, 120x600).
Please put in the ads a picture of the bottle (attached) and a picture of a slim woman/man (preferably woman, as I am targetting a largely female audience) in the advertisement.
As for the text of the ads, I'd like for there to be something like the following:
"Lose 15 lbs in 3 months"
"Lose weight with traditional Chinese medicine"
"Lose weight using ancient Chinese herbs"
Also please feel free to use other text using some of the articles on my site, which can be found at the following link:
http://www.tavrelo-example.com/
Thanks, and if you have any additional questions, please don't hesitate to ask.
Additional notes: would also like for you to follow the color scheme on my website (orange, green) for the most part, although please when submitting different ads make sure to include other color schemes, as some of those color schemes may work better for the ads than the green/orange color scheme.
I've also attached an ad from Vembrashed that should give you an idea of something similar I'm looking for (though please submit multiple ideas)!
Updates
Industry/Entity Type
Weight
Look and feel
Each slider illustrates characteristics of the customer's brand and the style your logo design should communicate.

```html
<!DOCTYPE html>
<html lang="en">
<head>
<meta charset="utf-8">
<title>Tavrelo Banner Set</title>
<link rel="stylesheet" href="https://fonts.googleapis.com/css2?family=Arimo:wght@400;700&family=Open+Sans:wght@400&display=swap">
<style>
  :root {
    --backdrop: #2b2b2b;
    --banner-white: #ffffff;
    --banner-sheen: #ececec;
    --headline-orange: #f15a0f;
    --body-text: #333333;
    --chevron-green: #7cb518;
    --button-green-top: #bde04a;
    --button-green-bottom: #97c51c;
    --button-text: #3d4a22;
    --skin-light: #f1d9cb;
    --skin-mid: #d9b5a1;
    --garment: #f4f2ee;
    --bottle-white: #f3f3f3;
    --bottle-shade: #cfcfcf;
    --herb-green: #6e8f3a;
  }
  html, body {
    margin: 0;
    padding: 0;
    width: 1200px;
    height: 1142px;
    overflow: hidden;
    background: var(--backdrop);
  }
  .board { position: relative; width: 1200px; height: 1142px; }
  .banner {
    position: absolute;
    overflow: hidden;
    background: linear-gradient(120deg, var(--banner-white) 0%, var(--banner-sheen) 35%, var(--banner-white) 55%, var(--banner-sheen) 100%);
    font-family: "Open Sans", Verdana, sans-serif;
    color: var(--body-text);
  }
  .headline {
    position: absolute;
    margin: 0;
    font-family: "Arimo", Arial, sans-serif;
    color: var(--headline-orange);
    line-height: 1;
    white-space: nowrap;
  }
  .headline .lead { display: block; font-weight: 700; }
  .headline .months { display: block; font-weight: 400; }
  .benefit {
    position: absolute;
    margin: 0;
    line-height: 1.6;
    white-space: nowrap;
  }
  .benefit .chevron {
    color: var(--chevron-green);
    font-family: "Arimo", Arial, sans-serif;
    font-weight: 700;
  }
  .order-button {
    position: absolute;
    display: flex;
    align-items: center;
    justify-content: center;
    border-radius: 6px;
    background: linear-gradient(var(--button-green-top), var(--button-green-bottom));
    color: var(--button-text);
    font-family: "Open Sans", Verdana, sans-serif;
    text-transform: uppercase;
    white-space: nowrap;
  }
  .model-photo {
    position: absolute;
    background: radial-gradient(ellipse at 55% 40%, var(--skin-light) 0%, var(--skin-mid) 45%, var(--garment) 75%, rgba(255,255,255,0) 100%);
  }
  .bottle-photo {
    position: absolute;
    border-radius: 14px 14px 18px 18px;
    background: linear-gradient(90deg, var(--bottle-shade) 0%, var(--bottle-white) 30%, var(--bottle-white) 70%, var(--bottle-shade) 100%);
  }
  .bottle-photo::after {
    content: "";
    position: absolute;
    left: 8%;
    right: 8%;
    top: 42%;
    height: 40%;
    background: linear-gradient(180deg, var(--bottle-white) 0%, var(--herb-green) 100%);
    opacity: 0.35;
    border-radius: 4px;
  }

  /* 600x450 banner */
  .banner-large { left: 61px; top: 57px; width: 829px; height: 622px; }
  .banner-large .headline { left: 243px; top: 62px; }
  .banner-large .lead { font-size: 31px; }
  .banner-large .months { font-size: 58px; margin-top: 8px; }
  .banner-large .benefit { left: 243px; font-size: 19px; padding-left: 32px; }
  .banner-large .benefit .chevron { position: absolute; left: 0; top: 0; }
  .banner-large .benefit-one { top: 218px; }
  .banner-large .benefit-two { top: 302px; left: 245px; }
  .banner-large .order-button { left: 348px; top: 477px; width: 185px; height: 57px; font-size: 20px; }
  .banner-large .model-photo { left: 0; top: 102px; width: 243px; height: 520px; }
  .banner-large .bottle-photo { left: 571px; top: 193px; width: 212px; height: 380px; }

  /* 120x600 skyscraper */
  .banner-skyscraper { left: 954px; top: 58px; width: 166px; height: 829px; }
  .banner-skyscraper .headline { left: 0; right: 0; top: 38px; text-align: center; }
  .banner-skyscraper .lead { font-size: 17px; }
  .banner-skyscraper .months { font-size: 26px; margin-top: 4px; }
  .banner-skyscraper .benefit { left: 0; right: 0; text-align: center; font-size: 14px; line-height: 1.6; }
  .banner-skyscraper .benefit-one { top: 128px; }
  .banner-skyscraper .benefit-two { top: 222px; }
  .banner-skyscraper .model-photo { left: 0; top: 308px; width: 158px; height: 290px; }
  .banner-skyscraper .bottle-photo.bottle-front { left: 24px; top: 564px; width: 76px; height: 126px; }
  .banner-skyscraper .bottle-photo.bottle-back { left: 86px; top: 594px; width: 60px; height: 98px; }
  .banner-skyscraper .order-button { left: 22px; top: 760px; width: 113px; height: 35px; font-size: 14px; }

  /* 250x250 square */
  .banner-square { left: 61px; top: 723px; width: 346px; height: 346px; }
  .banner-square .headline { left: 24px; top: 30px; }
  .banner-square .lead { font-size: 20px; }
  .banner-square .months { font-size: 35px; margin-top: 4px; }
  .banner-square .benefit { right: 23px; text-align: right; font-size: 15px; line-height: 1.45; }
  .banner-square .benefit-one { top: 118px; }
  .banner-square .benefit-two { top: 180px; }
  .banner-square .model-photo { left: 0; top: 104px; width: 119px; height: 242px; }
  .banner-square .bottle-photo { left: 84px; top: 179px; width: 77px; height: 152px; }
  .banner-square .order-button { left: 212px; top: 283px; width: 113px; height: 34px; font-size: 14px; }

  /* 300x250 rectangle */
  .banner-rectangle { left: 476px; top: 724px; width: 415px; height: 346px; }
  .banner-rectangle .headline { left: 41px; top: 29px; }
  .banner-rectangle .lead { font-size: 19px; }
  .banner-rectangle .months { font-size: 33px; margin-top: 4px; }
  .banner-rectangle .benefit { right: 19px; text-align: right; font-size: 17px; line-height: 1.35; }
  .banner-rectangle .benefit-one { top: 124px; }
  .banner-rectangle .benefit-two { top: 187px; }
  .banner-rectangle .model-photo { left: 0; top: 82px; width: 133px; height: 264px; }
  .banner-rectangle .bottle-photo { left: 122px; top: 160px; width: 80px; height: 166px; }
  .banner-rectangle .order-button { left: 297px; top: 289px; width: 100px; height: 31px; font-size: 12px; }
</style>
</head>
<body>
<main class="board">

  <section class="banner banner-large" aria-label="Tavrelo banner 600 by 450">
    <div class="model-photo" role="img" aria-label="Photo of a slim smiling woman in white underwear, arms raised behind her head"></div>
    <h2 class="headline"><span class="lead">LOSE 15LBS IN JUST</span><span class="months">3 MONTHS!!!</span></h2>
    <p class="benefit benefit-one"><span class="chevron">»</span>Lose weight with traditional<br>Chinese medicine</p>
    <p class="benefit benefit-two"><span class="chevron">»</span>Lose weight using ancient<br>Chinese herbs</p>
    <a class="order-button">Order now</a>
    <div class="bottle-photo" role="img" aria-label="Photo of a white Tavrelo supplement bottle with herbal label"></div>
  </section>

  <section class="banner banner-skyscraper" aria-label="Tavrelo banner 120 by 600">
    <h2 class="headline"><span class="lead">LOSE 15LBS IN</span><span class="months">3 MONTHS</span></h2>
    <p class="benefit benefit-one">Lose weight with<br>traditional<br>Chinese medicine</p>
    <p class="benefit benefit-two">Lose weight using<br>ancient Chinese<br>herbs</p>
    <div class="model-photo" role="img" aria-label="Photo of a slim smiling woman in white underwear"></div>
    <div class="bottle-photo bottle-back" role="img" aria-label="Photo of a small Tavrelo supplement bottle"></div>
    <div class="bottle-photo bottle-front" role="img" aria-label="Photo of a Tavrelo supplement bottle"></div>
    <a class="order-button">Order now</a>
  </section>

  <section class="banner banner-square" aria-label="Tavrelo banner 250 by 250">
    <h2 class="headline"><span class="lead">LOSE 15LBS IN</span><span class="months">3 MONTHS!!!</span></h2>
    <div class="model-photo" role="img" aria-label="Photo of a slim smiling woman in white underwear"></div>
    <div class="bottle-photo" role="img" aria-label="Photo of a Tavrelo supplement bottle"></div>
    <p class="benefit benefit-one"><span class="chevron">»</span> Lose weight with traditional<br>Chinese medicine</p>
    <p class="benefit benefit-two"><span class="chevron">»</span> Lose weight using<br>ancient Chinese<br>herbs</p>
    <a class="order-button">Order now</a>
  </section>

  <section class="banner banner-rectangle" aria-label="Tavrelo banner 300 by 250">
    <h2 class="headline"><span class="lead">LOSE 15LBS IN</span><span class="months">3 MONTHS!!!</span></h2>
    <div class="model-photo" role="img" aria-label="Photo of a slim smiling woman in white underwear"></div>
    <div class="bottle-photo" role="img" aria-label="Photo of a Tavrelo supplement bottle"></div>
    <p class="benefit benefit-one"><span class="chevron">»</span> Lose weight with traditional<br>Chinese medicine</p>
    <p class="benefit benefit-two"><span class="chevron">»</span> Lose weight using<br>ancient Chinese<br>herbs</p>
    <a class="order-button">Order now</a>
  </section>

</main>
</body>
</html>
```